Independent IT Consulting Professional. Looking for a clean crisp, somewhat traditional design. I have also attached the initial off-the-shelf design from PrintHaven. My company has grown quickly, and I would like to take the card to the next level. Should be sharp, mature, classy well laid-out and convey confidence. I don't think the off-the-shelf design does this. I like the logo I have for the time being, but if someone has something better in mind, I would be happy to consider an alternative. I would also like to see the color Cyan used in a small way, either with the logo or some other color treatment, as I feel like this is a modern color that I always liked, but never was able to make anything work with it.
Industry/Entity Type
It Company
Contact Information for Business Card
Carter J. Whitlow
Owner
TrellMark Solutions
2817 Ashborough Lane
Larkdale, NY 13990
(917) 555-0148
cwhitlow@trellmarksolutions.example
www.trellmarksolutions.example
Tagline: Business Technology Services and Consulting

```html
<!DOCTYPE html>
<html lang="en">
<head>
<meta charset="utf-8">
<title>TrellMark Solutions – Business Card</title>
<link rel="stylesheet" href="https://fonts.googleapis.com/css2?family=Open+Sans:wght@300;400;600;700&display=swap">
<style>
  :root {
    --page-bg: #3a3a3c;
    --card-white: #f4f4f4;
    --card-white-edge: #e2e2e2;
    --cyan: #1ba6cf;
    --cyan-deep: #1489b3;
    --navy: #1f4f9c;
    --ink: #2a2a2a;
    --ink-soft: #4a4a4a;
    --on-cyan: #dff3fa;
  }
  * { margin: 0; padding: 0; box-sizing: border-box; }
  html, body { width: 1200px; height: 900px; overflow: hidden; }
  body {
    background: var(--page-bg);
    font-family: "Open Sans", sans-serif;
    position: relative;
  }
  .card {
    position: absolute;
    left: 110px;
    top: 170px;
    width: 980px;
    height: 560px;
    overflow: hidden;
    background: linear-gradient(160deg, #ffffff 0%, var(--card-white) 50%, var(--card-white-edge) 100%);
    box-shadow: 0 18px 40px rgba(0,0,0,0.45);
  }
  .card-shapes { position: absolute; inset: 0; width: 100%; height: 100%; }
  .brand {
    position: absolute;
    left: 62px;
    top: 158px;
    display: flex;
    align-items: center;
    gap: 14px;
  }
  .brand-mark {
    width: 22px;
    height: 22px;
    background: var(--cyan);
  }
  .brand-name {
    font-weight: 700;
    font-size: 36px;
    color: var(--ink);
    letter-spacing: -0.5px;
  }
  .tagline {
    position: absolute;
    right: 90px;
    top: 62px;
    font-size: 18px;
    color: var(--ink-soft);
  }
  .person {
    position: absolute;
    right: 90px;
    top: 138px;
    text-align: right;
    color: var(--ink);
  }
  .person-name { font-size: 31px; font-weight: 300; line-height: 1.15; }
  .person-title { font-size: 18px; font-weight: 400; color: var(--ink-soft); line-height: 1.2; }
  .contact {
    position: absolute;
    right: 90px;
    top: 300px;
    text-align: right;
    color: var(--on-cyan);
    font-size: 22px;
    font-weight: 300;
    line-height: 32px;
  }
  .address {
    position: absolute;
    left: 75px;
    top: 424px;
    color: var(--on-cyan);
    font-size: 22px;
    font-weight: 300;
    line-height: 30px;
  }
  .address-company { font-weight: 600; }
</style>
</head>
<body>
  <div class="card">
    <svg class="card-shapes" viewBox="0 0 980 560" preserveAspectRatio="none" aria-hidden="true">
      <defs>
        <linearGradient id="cyanBand" x1="0" y1="0" x2="1" y2="1">
          <stop offset="0" stop-color="#1ba6cf"/>
          <stop offset="1" stop-color="#1489b3"/>
        </linearGradient>
      </defs>
      <path class="swoosh" fill="#1f4f9c"
            d="M0 350 C 200 345, 400 310, 560 262 C 420 308, 220 360, 0 385 Z"/>
      <path class="band" fill="url(#cyanBand)"
            d="M0 400 C 300 368, 650 310, 980 212 L980 560 L0 560 Z"/>
    </svg>

    <div class="brand">
      <span class="brand-mark"></span>
      <span class="brand-name">TrellMark Solutions</span>
    </div>

    <p class="tagline">Business Technology Services and Consulting</p>

    <div class="person">
      <p class="person-name">Carter J. Whitlow</p>
      <p class="person-title">Owner</p>
    </div>

    <div class="contact">
      <p>(917) 555-0148</p>
      <p>cwhitlow@trellmarksolutions.example</p>
      <p>www.trellmarksolutions.example</p>
    </div>

    <div class="address">
      <p class="address-company">TrellMark Solutions</p>
      <p>2817 Ashborough Lane</p>
      <p>Larkdale, NY 13990</p>
    </div>
  </div>
</body>
</html>
```